Graphic Design - Earth re-shaped with text added

We need a graphic design of earth shaped as an Apple. The Text would be: The Only Maple Hollow Realtors in the World. Earth to look 3D. Maybe "The Only Maple Hollow Realtors" curved at the top with ""In The World" over the apple earth. I would also like to see the same design with earth shaped correctly.

** I cannot find how to increase my project time to Wednesday of next week.

IT IS FIINE FOR THIS DESIGN TOO BE TURNED IN BY 3/18/2020

Please add Focused in the text. The only Apple Valley Focused Realtors... In The World.

Requirements
Must have
• Text to be big enough to be easily read.
Nice to have
• Modern style Text (no script)

```html
<!DOCTYPE html>
<html lang="en">
<head>
<meta charset="utf-8">
<title>The Only Maple Hollow Realtors in the World</title>
<link rel="stylesheet" href="https://fonts.googleapis.com/css2?family=Oswald:wght@500;700&display=swap">
<style>
  :root {
    --page-bg: #e9eaec;
    --poster-light: #f4f5f7;
    --poster-mid: #dfe1e5;
    --poster-dark: #c9ccd1;
    --brand-blue: #1565a6;
    --accent-orange: #f0a030;
    --ocean-deep: #0f2f6b;
    --ocean-mid: #1f58a8;
  }
  html, body {
    margin: 0;
    padding: 0;
    width: 1186px;
    height: 1200px;
    overflow: hidden;
    background: var(--page-bg);
  }
  .poster {
    position: absolute;
    left: 180px;
    top: 25px;
    width: 827px;
    height: 1150px;
    background: linear-gradient(100deg, var(--poster-dark) 0%, var(--poster-light) 45%, var(--poster-mid) 100%);
    box-shadow: 0 2px 10px rgba(0,0,0,0.12);
  }
  .poster-art {
    position: absolute;
    inset: 0;
    width: 827px;
    height: 1150px;
  }
  .headline {
    font-family: 'Oswald', sans-serif;
    font-weight: 700;
    fill: var(--brand-blue);
  }
  .brand-name {
    font-family: 'Oswald', sans-serif;
    font-weight: 700;
    fill: var(--brand-blue);
    letter-spacing: 1px;
  }
</style>
</head>
<body>
  <main class="poster">
    <svg class="poster-art" viewBox="0 0 827 1150" xmlns="http://www.w3.org/2000/svg">
      <defs>
        <radialGradient id="globe-fill" cx="0.42" cy="0.38" r="0.65">
          <stop offset="0" stop-color="#3f7a5a"/>
          <stop offset="0.35" stop-color="var(--ocean-mid)"/>
          <stop offset="0.8" stop-color="var(--ocean-deep)"/>
          <stop offset="1" stop-color="#081a40"/>
        </radialGradient>
        <radialGradient id="floor-shadow" cx="0.5" cy="0.5" r="0.5">
          <stop offset="0" stop-color="#5a5f68" stop-opacity="0.55"/>
          <stop offset="1" stop-color="#5a5f68" stop-opacity="0"/>
        </radialGradient>
        <linearGradient id="rule-line" x1="0" x2="1">
          <stop offset="0" stop-color="var(--accent-orange)" stop-opacity="0"/>
          <stop offset="0.5" stop-color="var(--accent-orange)"/>
          <stop offset="1" stop-color="var(--accent-orange)" stop-opacity="0"/>
        </linearGradient>
        <path id="headline-arc" d="M 50 418 A 920 920 0 0 1 780 418"/>
      </defs>

      <g class="brand-mark">
        <circle cx="272" cy="118" r="12" fill="var(--accent-orange)"/>
        <text class="brand-name" x="294" y="129" font-size="30" textLength="262">ORCHARD CREST HOMES</text>
      </g>

      <text class="headline" x="413" y="220" font-size="78" text-anchor="middle" textLength="275">THE ONLY</text>
      <rect x="280" y="234" width="267" height="2" fill="url(#rule-line)"/>

      <text class="headline" font-size="80">
        <textPath href="#headline-arc" startOffset="50%" text-anchor="middle" textLength="700">MAPLE HOLLOW REALTORS</textPath>
      </text>

      <ellipse cx="415" cy="912" rx="320" ry="26" fill="url(#floor-shadow)"/>
      <circle cx="415" cy="648" r="264" fill="url(#globe-fill)" role="img" aria-label="Three-dimensional Earth globe showing the Americas"/>

      <rect x="214" y="973" width="400" height="1.5" fill="url(#rule-line)"/>
      <text class="headline" x="414" y="1046" font-size="72" text-anchor="middle" textLength="396">IN THE WORLD</text>
      <rect x="214" y="1060" width="400" height="2" fill="url(#rule-line)"/>
    </svg>
  </main>
</body>
</html>
```